Business cards and stationary for mobile ultrasound company
Crestline Ultrasound Diagnostics
Business cards and stationary for mobile ultrasound company - Health
Creative Brief
Professional
Beatrice Kolwitz, RDCS, RVT
Presiden
PO Box 472906 Staten Island, NY 10314
855-617-LUMO
Beatrice@crestlinesono.example
www.crestlinesono.example
1) The name of the company is on the logo, so please use the logo in place of the company's name. The file will be uploaded later today (11/24/2014) But you can take a look at how this logo looks http://www.quorvadesk.example/contests/logo-for-a-mobil-ultrasond-company or search the contest Crestline Ultrasound Diagnostics - and review the winning logo design. 2) I will be interested in full variety of stationary, but most important are business card, envelopes (regular size), and letterhead/background (the others maybe, folders, large envelopes, etc) 3) I will need 2 business cards as there are 2 partners. Some of the info like name of the company, web address, address, etc. can stay the same, and some will be different. Info for my partner's card: Name: Gordon T Hasketh Title: VP cell: 917-405-2318 email address: Gordon@crestlinesono.example 4) Such info as web address and/or email addresses may change as the development of the project goes, if it does, I will ask to change it in the text of the cards. 5) Please keep colors withing the pallet of the logo (dark blue, royal blue, light shades of blue, red, silver/grey. Thank you!
BeatriceK BeatriceK
Hi! When using my name and title, please correct my typo I made in the title - President (I omitted the "t"), use the corrected word Thank you! Beatrice

```html
<!DOCTYPE html>
<html lang="en">
<head>
<meta charset="utf-8">
<title>Crestline Ultrasound Diagnostics — Stationery Set</title>
<link href="https://fonts.googleapis.com/css2?family=Montserrat:wght@400;600;700&display=swap" rel="stylesheet">
<style>
:root{
  --bg:#a9a9a9;
  --navy:#0b3564;
  --royal:#1b63a6;
  --sky:#63aee0;
  --ice:#e8f2fa;
  --red:#c8302c;
  --silver:#c9ccd1;
  --paper:#ffffff;
  --ink:#27415e;
  --rule:#d7dde4;
}
*{box-sizing:border-box;margin:0;padding:0}
html,body{width:1200px;height:430px;overflow:hidden;background:var(--bg);font-family:"Montserrat",sans-serif;color:var(--ink)}
.canvas{position:relative;width:1200px;height:430px}
.item{position:absolute;background:var(--paper);box-shadow:0 1px 3px rgba(0,0,0,.25);overflow:hidden}
.blue{background:linear-gradient(135deg,var(--royal) 0%,var(--navy) 100%);color:#fff}
.edge{position:absolute;right:0;top:0;bottom:0;width:5px;background:linear-gradient(180deg,var(--sky),var(--royal) 60%,var(--red))}
.edge.top{left:0;right:0;bottom:auto;width:auto;height:4px;background:linear-gradient(90deg,var(--sky),var(--royal) 60%,var(--red))}
.brand{display:inline-flex;align-items:center;gap:4px;font-weight:700;color:var(--royal);line-height:1;white-space:nowrap}
.brand .dot{width:.7em;height:.7em;border-radius:50%;background:var(--royal);flex:none}
.blue .brand{color:#fff}
.blue .brand .dot{background:#fff}
.tagline{font-size:6px;letter-spacing:.5px;color:var(--royal);margin-top:3px}
.blue .tagline{color:var(--ice)}
.fine{font-size:3.4px;line-height:1.5;white-space:nowrap}
.lines{position:absolute;left:12%;right:12%}
.lines i{display:block;height:2px;background:var(--rule);margin-bottom:5px}
.glow{position:absolute;border-radius:50%;background:radial-gradient(circle,rgba(255,255,255,.18),rgba(255,255,255,0) 70%)}

/* folder */
.folder-cover{left:5px;top:34px;width:235px;height:230px}
.folder-inside{left:240px;top:34px;width:240px;height:230px}
.folder-pocket{left:240px;top:264px;width:240px;height:144px;border-radius:0 0 4px 4px}
.folder-pocket-left{left:5px;top:264px;width:235px;height:144px;border-top:1px solid rgba(255,255,255,.25)}
.folder-cover .brand{position:absolute;left:26px;top:58px;font-size:24px}
.folder-cover .tagline{position:absolute;left:26px;top:86px}
.folder-inside .brand{position:absolute;left:62px;top:50px;font-size:22px}
.folder-inside .tagline{position:absolute;left:62px;top:76px}
.pocket-mark{position:absolute;left:50%;top:50%;transform:translate(-50%,-50%) rotate(180deg);font-size:20px}

.compliment{left:504px;top:41px;width:72px;height:67px}
.compliment .brand{position:absolute;left:8px;top:12px;font-size:9px}
.disc{left:595px;top:43px;width:65px;height:65px;border-radius:50%}
.disc::after{content:"";position:absolute;left:50%;top:50%;width:14px;height:14px;margin:-7px;border-radius:50%;background:var(--bg);box-shadow:0 0 0 4px var(--silver)}
.disc .band{position:absolute;left:0;right:0;bottom:0;height:22px;background:linear-gradient(90deg,var(--royal),var(--navy))}
.disc .brand{position:absolute;left:10px;top:12px;font-size:8px}
.notepad{left:700px;top:24px;width:72px;height:108px}
.notepad .brand{position:absolute;left:8px;top:10px;font-size:8px}

.card{width:72px;height:46px;padding:5px 8px 5px 5px}
.card .brand{font-size:8px}
.card-front{left:965px;top:36px}
.card-front .brand{position:absolute;left:10px;top:18px;font-size:9px}
.card-a{left:804px;top:36px}
.card-b{left:884px;top:36px}
.card .who{font-size:3.6px;font-weight:600;margin-top:5px;color:var(--navy);white-space:nowrap}

.env-small{left:792px;top:96px;width:92px;height:38px;padding:5px 8px 5px 5px}
.env-small .brand{font-size:7px}
.env-small .fine{margin-top:4px}
.env-mid{left:893px;top:96px;width:139px;height:40px;padding:6px}
.env-mid .brand{font-size:8px}
.env-mid .fine{margin-top:4px}

.letter{width:122px;height:204px;top:144px}
.letter .brand{position:absolute;left:14px;top:16px;font-size:10px}
.letter .foot{position:absolute;left:14px;bottom:8px;right:14px;font-size:4px;color:var(--royal)}
.letter-a{left:490px}
.letter-b{left:620px}
.letter-c{left:756px;top:144px;width:74px;height:156px}
.letter-c .brand{font-size:8px;left:9px}

.env-wide{left:845px;top:156px;width:192px;height:96px}
.env-wide .brand{position:absolute;left:12px;top:12px;font-size:10px}
.env-wide .addr{position:absolute;left:80px;top:52px;font-size:5px;line-height:1.5}
.env-back{left:845px;top:260px;width:192px;height:124px;background:var(--paper)}
.env-back svg{position:absolute;left:0;top:0}
.env-back .brand{position:absolute;left:50%;top:42%;transform:translateX(-50%);font-size:14px;color:#fff}
.env-back .brand .dot{background:#fff}

.phone{left:1098px;top:244px;width:30px;height:64px;border-radius:4px}
.phone .brand{position:absolute;left:50%;top:28px;transform:translateX(-50%);font-size:4px;gap:2px}
.tablet{left:1072px;top:336px;width:120px;height:80px;border-radius:4px}
.tablet .brand{position:absolute;left:10px;top:10px;font-size:9px}
.tablet .lines{top:28px}
</style>
</head>
<body>
<main class="canvas">

  <section class="item blue folder-cover">
    <div class="glow" style="left:60px;top:100px;width:200px;height:200px"></div>
    <span class="brand"><span class="dot"></span>Crestline</span>
    <p class="tagline">Mobile Ultrasound Services</p>
  </section>
  <section class="item folder-inside">
    <span class="brand"><span class="dot"></span>Crestline</span>
    <p class="tagline">Ultrasound Diagnostics</p>
    <div class="edge"></div>
  </section>
  <section class="item blue folder-pocket-left">
    <span class="brand pocket-mark"><span class="dot"></span>Crestline</span>
  </section>
  <section class="item blue folder-pocket">
    <span class="brand pocket-mark"><span class="dot"></span>Crestline</span>
  </section>

  <div class="item compliment"><span class="brand"><span class="dot"></span>Crestline</span><div class="edge"></div></div>
  <div class="item disc"><span class="brand"><span class="dot"></span>Crestline</span><div class="band"></div></div>
  <div class="item notepad">
    <span class="brand"><span class="dot"></span>Crestline</span>
    <div class="lines" style="top:34px"><i></i><i></i><i></i><i></i><i></i><i></i><i></i><i></i></div>
    <div class="edge top" style="top:auto;bottom:0"></div>
  </div>

  <article class="item card card-a">
    <span class="brand"><span class="dot"></span>Crestline</span>
    <p class="who">Beatrice Kolwitz, RDCS, RVT</p>
    <p class="fine">President<br>855-617-LUMO<br>Beatrice@crestlinesono.example</p>
    <div class="edge"></div>
  </article>
  <article class="item card card-b">
    <span class="brand"><span class="dot"></span>Crestline</span>
    <p class="who">Gordon T Hasketh</p>
    <p class="fine">VP · 917-405-2318<br>Gordon@crestlinesono.example</p>
    <div class="edge"></div>
  </article>
  <article class="item card blue card-front"><span class="brand"><span class="dot"></span>Crestline</span></article>

  <div class="item env-small"><span class="brand"><span class="dot"></span>Crestline</span><p class="fine">PO Box 472906<br>Staten Island, NY 10314</p><div class="edge"></div></div>
  <div class="item env-mid"><span class="brand"><span class="dot"></span>Crestline</span><p class="fine">www.crestlinesono.example</p><div class="edge"></div></div>

  <article class="item letter letter-a">
    <span class="brand"><span class="dot"></span>Crestline</span>
    <div class="lines" style="top:60px"><i></i><i></i><i></i><i></i><i></i><i></i><i></i><i></i><i></i><i></i><i></i><i></i></div>
    <p class="foot">PO Box 472906 Staten Island, NY 10314 · 855-617-LUMO · www.crestlinesono.example</p>
    <div class="edge"></div>
  </article>
  <article class="item letter letter-b">
    <span class="brand"><span class="dot"></span>Crestline</span>
    <div class="lines" style="top:48px;right:50%"><i></i><i></i><i></i></div>
    <div class="lines" style="top:80px"><i></i><i></i><i></i><i></i><i></i><i></i><i></i><i></i><i></i><i></i></div>
    <p class="foot">PO Box 472906 Staten Island, NY 10314 · 855-617-LUMO · www.crestlinesono.example</p>
    <div class="edge"></div>
  </article>
  <article class="item letter letter-c">
    <span class="brand"><span class="dot"></span>Crestline</span>
    <div class="lines" style="top:44px"><i></i><i></i><i></i><i></i><i></i><i></i><i></i><i></i></div>
    <div class="edge"></div>
  </article>

  <article class="item env-wide">
    <span class="brand"><span class="dot"></span>Crestline</span>
    <p class="addr">PO Box 472906<br>Staten Island, NY 10314</p>
    <div class="edge"></div>
  </article>
  <article class="item env-back">
    <svg width="192" height="124" viewBox="0 0 192 124" aria-hidden="true">
      <defs><linearGradient id="flap" x1="0" y1="0" x2="1" y2="1"><stop offset="0" stop-color="#1b63a6"/><stop offset="1" stop-color="#0b3564"/></linearGradient></defs>
      <path d="M0 0H192V40L110 96Q96 104 82 96L0 40Z" fill="url(#flap)"/>
      <path d="M0 124L80 80M192 124L112 80" stroke="#d7dde4" stroke-width="1" fill="none"/>
    </svg>
    <span class="brand"><span class="dot"></span>Crestline</span>
  </article>

  <div class="item blue phone"><span class="brand"><span class="dot"></span>Crestline</span></div>
  <div class="item tablet">
    <span class="brand"><span class="dot"></span>Crestline</span>
    <div class="lines"><i></i><i></i><i></i><i></i><i></i><i></i></div>
    <div class="edge"></div>
  </div>

</main>
</body>
</html>
```